Corvane Storage Solutions
Your residential property self storage partner
Storage
Corvane Storage Solutions converts unused space in apartment and condominium buildings (primarily basements, unused rooms and parking garages) into attractive (they look like storage units at Kestrel Vaults, not chicken wire), functional self-storage units. We design the plan, construct and install units, and manage the rentals of the units to the buildings tenants.
Convenient. Secure. Practical. Innovative.
Audience is apartment and condo building managers and their residents. Residents will be Middle to Upper Class Socioecenomic range, Metropolitan. 20-75 years. equally men + women.
Like: clean and simple are a must. Want some green to tie logo in but do not want a predominantly green website. No red, orange or yellow.
"tabs" are too generic looking- would like something more unique.
Dislike: text heavy
Service Oriented
gray and/ or white
blue
black and green
top
http://www31.talmirex.com/content/talmirexglobalhome/ghp_business.aspx
quarbeck.com
http://www.dunmerefieldplaza.com/shopping/
Another website we like is www.fennicor.com
Our Logo is in Trebuchet MS. We are not sure if we like all the same font for website or use of a different font that complements the logo font. Will leave that to designer.
Please use logo.
Please use an image of storage units as well as other stock images as appropriate. I have photos of our units that I would like to use but Im not sure if they will integrate well. The focus of those images is how the storage units fir into a parking garage
Site should be clean and minimalist. we help minimize clutter in condos/apts and offer a clean, attractive solution, want to be sure that the site sends the same message in look and feel.
logo
logo variation
logo variation 2
lock and key clip art
box clip art
box2 clip art
lock and credit card image
lock and key image
inspiration- page image
inspiration- image

```html
<!DOCTYPE html>
<html lang="en">
<head>
<meta charset="utf-8">
<title>Corvane Storage Solutions – About Us</title>
<link href="https://fonts.googleapis.com/css2?family=Francois+One&family=Open+Sans:wght@400;600;700&display=swap" rel="stylesheet">
<style>
  :root {
    --green: #6cbd2c;
    --green-dark: #4e9a17;
    --green-light: #a6dc62;
    --ink: #333333;
    --text: #3c3c3c;
    --nav: #555555;
    --ribbon: #e9e9e9;
    --white: #ffffff;
  }
  * { margin: 0; padding: 0; box-sizing: border-box; }
  html, body { width: 1200px; height: 802px; overflow: hidden; }
  body {
    position: relative;
    font-family: "Open Sans", Arial, sans-serif;
    background: linear-gradient(to bottom, #ffffff 0, #ffffff 160px, #f0f0f0 300px, #e4e4e4 690px);
    color: var(--text);
  }
  .footer-band {
    position: absolute; left: 0; right: 0; top: 700px; height: 102px;
    background: linear-gradient(to bottom, var(--green-light) 0, var(--green) 45%, var(--green-dark) 100%);
  }

  /* Brand */
  .brand { position: absolute; left: 150px; top: 40px; display: flex; align-items: center; gap: 16px; }
  .brand-mark { width: 110px; height: 110px; border-radius: 50%; background: var(--ink); }
  .brand-name {
    font-family: "Open Sans", Arial, sans-serif; font-weight: 700;
    color: var(--ink); font-size: 30px; line-height: 1.05; letter-spacing: 0.5px;
  }

  /* Navigation */
  .main-nav { position: absolute; top: 0; left: 0; height: 130px; }
  .main-nav a {
    position: absolute; top: 88px; white-space: nowrap;
    font-size: 12px; font-weight: 700; color: var(--nav); text-decoration: none;
  }
  .main-nav a.active { color: var(--white); }
  .nav-tab {
    position: absolute; left: 650px; top: 0; width: 78px; height: 125px;
    background: linear-gradient(to bottom, var(--green-light), var(--green) 60%, var(--green-dark));
    border-radius: 0 0 4px 4px;
  }

  /* Content panel */
  .panel {
    position: absolute; left: 149px; top: 199px; width: 912px; height: 534px;
    background: var(--white);
    box-shadow: 0 0 14px rgba(0,0,0,0.12);
  }

  /* Section ribbons */
  .section-menu { position: absolute; left: 132px; top: 233px; width: 460px; }
  .ribbon {
    position: absolute; left: 0; height: 96px; width: 444px;
    font-family: "Francois One", "Arial Narrow", sans-serif;
    font-size: 58px; line-height: 96px; padding-left: 46px;
    color: var(--green);
    background: linear-gradient(to bottom, #f7f7f7, var(--ribbon) 70%, #dcdcdc);
    box-shadow: 0 6px 8px rgba(0,0,0,0.12);
    clip-path: polygon(0 0, 96% 0, 100% 50%, 96% 100%, 0 100%);
  }
  .ribbon.current {
    color: var(--white); height: 120px; line-height: 120px; width: 452px;
    background: linear-gradient(to bottom, var(--green-light), var(--green) 55%, var(--green-dark));
  }
  .ribbon-who   { top: 0; }
  .ribbon-what  { top: 120px; }
  .ribbon-how   { top: 240px; }
  .ribbon-quote { top: 352px; }

  /* Article */
  .article { position: absolute; left: 629px; top: 232px; width: 380px; }
  .article h1 {
    font-family: "Open Sans", Arial, sans-serif; font-weight: 600;
    color: var(--green); font-size: 30px; line-height: 1.3; margin-bottom: 14px;
  }
  .article p { font-size: 11.6px; line-height: 18px; text-align: justify; margin-bottom: 18px; }

  .scroll-track {
    position: absolute; left: 1016px; top: 240px; width: 6px; height: 420px;
    background: var(--green); border-radius: 3px;
  }
  .read-more {
    position: absolute; left: 852px; top: 622px; width: 134px; height: 38px;
    border-radius: 19px; border: 1px solid #bcbcbc;
    background: linear-gradient(to bottom, #ffffff, #d8d8d8);
    font-size: 17px; font-weight: 700; color: #777; text-align: center; line-height: 36px;
    text-decoration: none;
  }

  /* Footer */
  .site-footer { position: absolute; left: 0; top: 744px; width: 1200px; z-index: 2; }
  .footer-nav { text-align: center; font-size: 10px; line-height: 14px; color: var(--white); }
  .footer-nav a { color: var(--white); text-decoration: none; margin: 0 6px; }
  .footer-legal { margin-top: 10px; text-align: center; font-size: 10px; line-height: 14px; color: var(--white); }
</style>
</head>
<body>
  <div class="footer-band"></div>

  <header>
    <div class="brand">
      <div class="brand-mark"></div>
      <div class="brand-name">Corvane<br>Storage Solutions</div>
    </div>
    <div class="nav-tab"></div>
    <nav class="main-nav">
      <a href="#" style="left:604px">HOME</a>
      <a href="#" class="active" style="left:660px">ABOUT US</a>
      <a href="#" style="left:748px">SERVICES</a>
      <a href="#" style="left:826px">SOLUTIONS</a>
      <a href="#" style="left:914px">DETAILS</a>
      <a href="#" style="left:985px">CONTACT US</a>
    </nav>
  </header>

  <main class="panel"></main>

  <nav class="section-menu">
    <div class="ribbon ribbon-who">WHO WE ARE</div>
    <div class="ribbon ribbon-how">HOW WE DO IT</div>
    <div class="ribbon ribbon-quote">GET A QUOTE</div>
    <div class="ribbon ribbon-what current">WHAT WE DO</div>
  </nav>

  <article class="article">
    <h1>What We Do It?</h1>
    <p>Corvane Storage Solutions converts unused space in apartment and condominium buildings (primarily basements, unused rooms and parking garages) into attractive (they look like storage units at Kestrel Vaults, not chicken wire), functional self-storage units.</p>
    <p>We design the plan, construct and install units, and manage the rentals of the units to the buildings tenants.Convenient. Secure. Corvane Storage Solutions converts unused space in apartment and condominium buildings.</p>
    <p>Corvane Storage Solutions converts unused space in apartment and condominium buildings (primarily basements, unused rooms and parking garages) into attractive (they look like storage units at Kestrel Vaults, not chicken wire), functional self-storage units.</p>
  </article>
  <div class="scroll-track"></div>
  <a href="#" class="read-more">Read More</a>

  <footer class="site-footer">
    <div class="footer-nav">
      <a href="#">Home</a>|<a href="#">About Us</a>|<a href="#">Services</a>|<a href="#">Solutions</a>|<a href="#">Products</a>|<a href="#">Contact Us</a>
    </div>
    <div class="footer-legal">© 2011 Corvane Storage Solutions &nbsp;|&nbsp; 4410 Marrow Glen Ave Suite 120, CO 80512 &nbsp;|&nbsp; map &nbsp;|&nbsp; Website Credits</div>
  </footer>
</body>
</html>
```